Apartment Investor Business Card Design

Need a new business card designed for my multifamily investment company

Industry/Entity Type

Real Estate

Contact Information for Business Card

Marlow Pickett - President & CEO
Brightfield Capital, LLC
4870 North 52nd Avenue, Ste 150
Omaha, NE 68231
(402) 555-0193
Marlow@brightfieldcapitalmidwest.example
Www.BrightfieldCapitalMidwest.example

Colors
3176b5

```html
<!DOCTYPE html>
<html lang="en">
<head>
<meta charset="utf-8">
<title>Brightfield Capital – Business Card</title>
<link rel="stylesheet" href="https://fonts.googleapis.com/css2?family=Cinzel:wght@500;700&family=Poppins:wght@300;400&display=swap">
<style>
  :root {
    --brand-blue: #3176b5;
    --band-blue: #5b92d6;
    --card-black: #0b0b0d;
    --card-white: #ffffff;
    --ink: #111114;
    --ink-soft: #3a3a3f;
    --backdrop: #2b2d31;
    --rule: #1a1a1a;
  }
  * { box-sizing: border-box; margin: 0; padding: 0; }
  html, body { width: 1200px; height: 900px; overflow: hidden; }
  body {
    background: var(--backdrop);
    position: relative;
    font-family: "Poppins", sans-serif;
  }
  .card {
    position: absolute;
    width: 525px;
    height: 300px;
    border-radius: 22px;
    overflow: hidden;
  }

  /* Back of card */
  .card-back {
    left: 600px;
    top: 90px;
    background: var(--card-black);
  }
  .card-back .brand {
    position: absolute;
    left: 0; right: 0; top: 95px;
    display: flex;
    align-items: center;
    justify-content: center;
    gap: 14px;
  }
  .brand-mark {
    width: 18px; height: 18px;
    background: var(--brand-blue);
  }
  .card-back .brand-name {
    font-family: "Cinzel", serif;
    font-weight: 500;
    font-size: 36px;
    letter-spacing: 1px;
    color: var(--card-white);
  }
  .address-band {
    position: absolute;
    left: 0; right: 0; bottom: 0;
    height: 62px;
    background: var(--band-blue);
    display: flex;
    align-items: center;
    justify-content: center;
    font-size: 14px;
    color: var(--ink);
  }
  .address-band::before {
    content: "";
    position: absolute;
    left: 50%; top: -9px;
    margin-left: -9px;
    border-left: 9px solid transparent;
    border-right: 9px solid transparent;
    border-bottom: 9px solid var(--band-blue);
  }

  /* Front of card */
  .card-front {
    left: 75px;
    top: 500px;
    background: var(--card-white);
    padding: 34px 40px;
  }
  .card-front .brand {
    display: flex;
    align-items: center;
    gap: 10px;
  }
  .card-front .brand-mark { width: 14px; height: 14px; }
  .card-front .brand-name {
    font-family: "Cinzel", serif;
    font-weight: 500;
    font-size: 20px;
    color: var(--ink);
  }
  .divider {
    height: 1px;
    margin: 18px 0 16px;
    background: linear-gradient(90deg, transparent, var(--rule) 15%, var(--rule) 85%, transparent);
  }
  .person-name {
    font-family: "Cinzel", serif;
    font-weight: 700;
    font-size: 25px;
    color: var(--ink);
    line-height: 1.1;
  }
  .person-title {
    font-weight: 300;
    font-size: 16px;
    color: var(--ink-soft);
    margin-bottom: 14px;
  }
  .contact-line {
    font-weight: 300;
    font-size: 14px;
    color: var(--ink-soft);
    line-height: 1.45;
  }
</style>
</head>
<body>
  <section class="card card-back" aria-label="Card back">
    <div class="brand">
      <span class="brand-mark"></span>
      <span class="brand-name">Brightfield Capital</span>
    </div>
    <div class="address-band">4870 North 52nd Avenue, Ste 150, Omaha, NE 68231</div>
  </section>

  <section class="card card-front" aria-label="Card front">
    <div class="brand">
      <span class="brand-mark"></span>
      <span class="brand-name">Brightfield Capital</span>
    </div>
    <div class="divider"></div>
    <p class="person-name">Marlow Pickett</p>
    <p class="person-title">President &amp; CEO</p>
    <p class="contact-line">(402) 555-0193</p>
    <p class="contact-line">Marlow@brightfieldcapitalmidwest.example</p>
    <p class="contact-line">www.BrightfieldCapitalMidwest.example</p>
  </section>
</body>
</html>
```